Redesign of TaskHarbor.com website

Our website was initially developed 6+ years ago and has been maintained by several different designers. As a result, it is overly complex, inconsistent format/layout and the content is not well structured/easy to navigate

We need the site redeveloped with a more modern look and feel, simpler content structure and ability to implement new/improved tools, such as: Dynamic Forms, Sales Funnels, Landing Pages, improved metadata of our pages and posts, improved SEO/Page ranking, etc.

We currently use DealRiver CRM, Steady Reach for marketing automation and GridPilot forms. We are investigating Floxen for workflow integration which could extend to our website.

Our current website is developed in WordPress, ideally we will stick with this platform, but we’re happy to consider other CMS' if strongly recommended. We may decide to remove/consolidate some of the pages and/or content as part of this re-design.

We don't want to rebrand (ie change corporate logo, colours scheme etc) as part of this website redevelopment and it is critical that we don't lose our current Page Ranking, SEO rankings, backlink benefits, etc as part of this redevelopment.

Sites we like the feel/design of are: boardwiley.com, tallypoint.com and rankgrove.com

Target Market(s)

Corporate, Enterprise and Government B2B clients.

Coding

Coded - Design and coding required

Number of Pages Required

5+ page

Font styles to use
Sans Serif

Colors
ffffff
ec1f27

Requirements
Must have
• Must retain the majority of content on our existing website (although we may re-write some of it as part of this redesign process).
Nice to have
• See above "Project Description"
Should not have

```html
<!DOCTYPE html>
<html lang="en">
<head>
<meta charset="utf-8">
<title>TaskHarbor — Your trusted advisor</title>
<link rel="stylesheet" href="https://fonts.googleapis.com/css2?family=Quicksand:wght@400;500;600;700&family=Montserrat:wght@500;600;700;800&display=swap">
<style>
:root{
  --header:#3a3a3b;
  --black:#000;
  --about:#1e1d1f;
  --inst:#1a191b;
  --services:#555658;
  --blue:#00aeef;
  --red:#c4141a;
  --brand-red:#ec1f27;
  --white:#fff;
  --navy:#121923;
  --footer:#1f1f20;
  --muted:#d8d8d8;
}
*{box-sizing:border-box;margin:0;padding:0}
html,body{width:1200px;height:3805px;overflow:hidden;background:#000}
body{position:relative;font-family:'Quicksand',sans-serif;color:var(--white)}
.abs{position:absolute}
section,header,footer{position:absolute;left:0;width:1200px}

/* header */
.site-header{top:0;height:97px;background:var(--header)}
.brand{position:absolute;display:flex;align-items:center;gap:8px}
.brand-dot{width:34px;height:34px;border-radius:50%;background:var(--brand-red)}
.brand-name{font-family:'Quicksand',sans-serif;font-weight:600;font-size:36px;color:var(--white);line-height:1}
.brand-tag{font-size:10px;color:var(--muted);display:block;text-align:right;margin-top:2px}
.site-header .brand{left:88px;top:22px}
.nav{position:absolute;right:88px;top:40px;display:flex;gap:22px;font-size:15px;font-weight:500;letter-spacing:.3px}
.nav a{color:var(--white);text-decoration:none;padding-bottom:4px}
.nav a.active{border-bottom:2px solid var(--blue)}

/* hero */
.hero{top:97px;height:461px;background:var(--black)}
.hero-visual{position:absolute;left:660px;top:100px;width:460px;height:340px;background:radial-gradient(ellipse at 60% 45%,#ff6a3a 0%,#c0282d 25%,#3a0a10 55%,#000 75%)}
.hero-title{position:absolute;left:86px;top:170px;font-size:33px;font-weight:600;line-height:41px;letter-spacing:.5px}
.hero-sub{position:absolute;left:86px;top:253px;font-size:10.5px;line-height:14px;width:270px}
.slider-dots{position:absolute;top:447px;left:494px;display:flex;gap:25px}
.slider-dots span{width:53px;height:5px;background:#777}
.slider-dots span.on{background:var(--blue)}

/* shared */
.accent-bar{position:absolute;width:110px;height:9px;background:var(--blue)}
.sec-title{position:absolute;font-size:50px;font-weight:500;line-height:1}
.sec-text{position:absolute;font-size:15px;line-height:19px}
.feature{position:absolute;display:flex;gap:8px}
.feature h4{font-size:20px;font-weight:500;line-height:22px}
.feature p{font-size:11px;line-height:14px;width:330px;margin-top:4px}
.medal{width:36px;height:36px;border-radius:50%;background:radial-gradient(circle at 40% 40%,#ffd54a,#e59d0b);color:#6b4300;font-weight:700;font-size:18px;display:flex;align-items:center;justify-content:center;flex:none}
.case{width:38px;height:30px;border-radius:5px;background:linear-gradient(#ffb32e,#e6820b);flex:none;margin-top:4px;position:relative}
.case::before{content:"";position:absolute;left:12px;top:-6px;width:14px;height:7px;border:3px solid #e6820b;border-bottom:none;border-radius:3px 3px 0 0}
.photo{position:absolute}

/* about */
.about{top:558px;height:534px;background:var(--about)}
/* institutional */
.institutional{top:1092px;height:546px;background:var(--inst)}

/* services */
.services{top:1638px;height:597px;background:var(--services)}
.btn-view{position:absolute;left:782px;top:157px;width:268px;height:48px;background:var(--blue);color:#111;font-size:25px;font-weight:600;display:flex;align-items:center;justify-content:center}
.svc-col{position:absolute;top:308px;width:300px}
.svc-col h3{font-size:20px;font-weight:700;margin-bottom:6px}
.svc-col li{list-style:none;font-size:13px;line-height:23px;color:#eee}
.btn-learn{display:inline-block;margin-top:12px;background:var(--red);color:var(--white);font-family:'Montserrat',sans-serif;font-size:13px;font-weight:600;padding:7px 18px}

/* fun facts */
.funfacts{top:2235px;height:330px;background:var(--black);text-align:center}
.ff-title{position:absolute;left:0;width:1200px;top:73px;font-family:'Montserrat',sans-serif;font-size:50px;font-weight:700;letter-spacing:6px}
.ff-sub{position:absolute;left:250px;width:700px;top:133px;font-size:15px;font-weight:700;line-height:23px}
.fact{position:absolute;top:230px;width:240px;text-align:center}
.fact b{display:block;color:var(--blue);font-size:20px;font-weight:600}
.fact span{display:block;font-size:20px;margin-top:4px}

/* testimonials */
.testimonials{top:2565px;height:676px;background:linear-gradient(110deg,#f3f3f5 0%,#e4e6ec 45%,#d6dbe4 100%);color:#111}
.contact-band{top:3241px;height:269px;background:var(--red)}
.person{position:absolute;left:138px;top:58px;width:337px;height:462px;background:linear-gradient(#9aa3b3,#2e3d5c);border-radius:120px 120px 0 0}
.quote-mark{position:absolute;left:422px;top:10px;font-family:'Montserrat',sans-serif;font-size:150px;font-weight:800;color:#777;line-height:1}
.t-title{position:absolute;left:510px;top:85px;font-size:40px;font-weight:500;line-height:48px}
.t-text{position:absolute;left:514px;top:210px;width:510px;font-size:14px;line-height:20px;color:#333}
.t-name{position:absolute;left:514px;top:313px;font-size:16px;font-weight:600}
.t-role{position:absolute;left:514px;top:340px;font-size:16px;color:#333}
.arrow-btn{position:absolute;top:392px;width:36px;height:36px;border-radius:50%;background:var(--red);color:var(--white);display:flex;align-items:center;justify-content:center}

/* contact card */
.contact-card{position:absolute;left:160px;top:3086px;width:908px;height:358px;background:var(--navy)}
.cc-kicker{position:absolute;left:40px;top:37px;font-family:'Montserrat',sans-serif;font-size:9px;font-weight:700}
.cc-title{position:absolute;left:40px;top:66px;font-family:'Montserrat',sans-serif;font-size:30px;font-weight:800;line-height:35px}
.cc-text{position:absolute;left:40px;top:152px;font-size:11px}
.cc-addr{position:absolute;left:40px;top:288px;font-size:12px;line-height:14px}
.socials{position:absolute;display:flex;gap:9px}
.socials span{width:17px;height:17px;border-radius:50%;background:var(--white)}
.field-label{position:absolute;font-size:9px;color:#ddd}
.field{position:absolute;background:var(--white);height:31px}
.btn-touch{position:absolute;left:465px;top:282px;width:115px;height:28px;background:var(--red);font-family:'Montserrat',sans-serif;font-size:10px;font-weight:700;display:flex;align-items:center;justify-content:center}

/* footer */
.site-footer{top:3510px;height:295px;background:var(--footer)}
.f-about{position:absolute;left:76px;top:34px;width:380px;font-size:15px;line-height:20px;color:#eee}
.f-links{position:absolute;top:33px;list-style:none;font-family:'Montserrat',sans-serif;font-size:9.5px;font-weight:700}
.f-links li{height:39px}
.f-divider{position:absolute;left:605px;top:22px;width:3px;height:255px;background:var(--blue)}
.f-right{position:absolute;right:85px;text-align:right;font-size:15px;line-height:20px}
.copyright{position:absolute;left:76px;top:265px;font-size:13px;color:#eee}
.site-footer .brand{right:85px;top:205px}
</style>
</head>
<body>

<header class="site-header">
  <div class="brand">
    <span class="brand-dot"></span>
    <div><span class="brand-name">taskharbor</span><span class="brand-tag">your trusted advisor</span></div>
  </div>
  <nav class="nav">
    <a class="active">HOME</a><a>ABOUT</a><a>SERVICES</a><a>CLIENTS</a><a>RESOURCES</a><a>BLOG</a><a>CONTACT US</a>
  </nav>
</header>

<section class="hero">
  <div class="hero-visual" role="img" aria-label="Glowing open laptop on a dark surface with red and orange light"></div>
  <svg class="abs" style="left:0;top:0" width="420" height="461" viewBox="0 0 420 461">
    <polygon points="291,83 368,261 189,342 112,162" fill="none" stroke="#fff" stroke-width="2"/>
  </svg>
  <h1 class="hero-title">LET’S BUILD<br>SOMETHING.</h1>
  <p class="hero-sub">We work with the most innovative solution on the market to help you get the best result</p>
  <div class="slider-dots"><span class="on"></span><span></span><span></span></div>
</section>

<section class="about">
  <div class="accent-bar" style="left:88px;top:77px"></div>
  <h2 class="sec-title" style="left:86px;top:117px">About Us</h2>
  <p class="sec-text" style="left:88px;top:182px;width:450px">For over 8 years we have been developing digital solutions for companies looking to gain better visibility on the internet.</p>
  <div class="feature" style="left:90px;top:297px"><span class="medal">1</span><div><h4>Quality</h4><p>Everything we do has the commitment of a well trained Band motivated team.</p></div></div>
  <div class="feature" style="left:90px;top:405px"><span class="case"></span><div><h4>Experience</h4><p>Focused on results we seek to raise the level of our customers.</p></div></div>
  <div class="photo" style="left:568px;top:110px;width:547px;height:364px;background:linear-gradient(135deg,#b9b9b5,#7a5238 45%,#5d3b27 70%,#c8c6c2)" role="img" aria-label="Team meeting around a wooden table with laptops, seen from above"></div>
</section>

<section class="institutional">
  <div class="photo" style="left:86px;top:93px;width:528px;height:361px;background:linear-gradient(135deg,#1b6f7d,#5cc3d1 45%,#1e8a99 70%,#0d3f4a)" role="img" aria-label="Hands typing on a laptop with a glowing digital globe network"></div>
  <div class="accent-bar" style="left:693px;top:94px"></div>
  <h2 class="sec-title" style="left:692px;top:133px">Institutional</h2>
  <p class="sec-text" style="left:693px;top:200px;width:460px">Get to know a little of our history and the road we traveled that took us to the level we are today.</p>
  <div class="feature" style="left:694px;top:290px"><span class="medal">1</span><div><h4>Tradition</h4><p>Everything we do has the commitment of a well trained Band motivated team.</p></div></div>
  <div class="feature" style="left:694px;top:397px"><span class="case"></span><div><h4>Innovation</h4><p>Focused on results we seek to raise the level of our customers.</p></div></div>
</section>

<section class="services">
  <div class="accent-bar" style="left:88px;top:50px"></div>
  <h2 class="sec-title" style="left:87px;top:89px">Services</h2>
  <p class="sec-text" style="left:88px;top:155px;width:500px">Our services are tailored to suit your business: regardless of size, industry and demographic.</p>
  <p class="sec-text" style="left:88px;top:210px;width:520px">We deliver consistent results, whether we’re working with the largest brand names around the world, or the smallest local company.</p>
  <div class="btn-view">VIEW MORE</div>

  <div class="svc-col" style="left:158px">
    <h3>Software Solutions</h3>
    <ul><li>- Digital Information Security Policy</li><li>- Information Security Management</li><li>- Cyber Security Awareness Training</li><li>- Security Review and Assessment</li><li>- Security Risk Management</li><li>- Vulnerability Identification &amp; Testing</li><li>- Penetration Testing</li><li>- Network Traffic Analysis</li></ul>
    <span class="btn-learn">LEARN MORE</span>
  </div>
  <div class="svc-col" style="left:481px">
    <h3>Data Management</h3>
    <ul><li>- Digital Information Security Policy</li><li>- Information Security Management</li><li>- Cyber Security Awareness Training</li><li>- Security Review and Assessment</li><li>- Security Risk Management</li><li>- Vulnerability Identification &amp; Testing</li><li>- Penetration Testing</li><li>- Network Traffic Analysis</li></ul>
    <span class="btn-learn">LEARN MORE</span>
  </div>
  <div class="svc-col" style="left:807px">
    <h3>Security Management</h3>
    <ul><li>- Digital Information Security Policy</li><li>- Information Security Management</li><li>- Cyber Security Awareness Training</li><li>- Security Review and Assessment</li><li>- Security Risk Management</li><li>- Vulnerability Identification &amp; Testing</li><li>- Penetration Testing</li><li>- Network Traffic Analysis</li></ul>
    <span class="btn-learn">LEARN MORE</span>
  </div>
</section>

<section class="funfacts">
  <h2 class="ff-title">FUN FACTS</h2>
  <p class="ff-sub">Over the years we have done many things that we are proud of. This motivates us to continue looking for new challenges in order to improve our services</p>
  <div class="fact" style="left:120px"><b>488</b><span>Great Projects</span></div>
  <div class="fact" style="left:358px"><b>228</b><span>Innovations</span></div>
  <div class="fact" style="left:624px"><b>903</b><span>Cups of Coffee</span></div>
  <div class="fact" style="left:885px"><b>888</b><span>Happy Customer</span></div>
</section>

<section class="testimonials">
  <div class="person" role="img" aria-label="Portrait of a business partner in a suit with arms crossed"></div>
  <div class="quote-mark">“</div>
  <h2 class="t-title">Real Testimonials<br>from our partners</h2>
  <p class="t-text">It was good to work with you. There are very few true professional organizations such as yours, in this industry. I wish you all the best and I would indeed enjoy working with you again.</p>
  <p class="t-name">Martin Hale</p>
  <p class="t-role">Head of Infrastructure Services - Northwind Systems</p>
  <div class="arrow-btn" style="left:979px"><svg width="12" height="12" viewBox="0 0 12 12"><path d="M8 1 3 6l5 5" fill="none" stroke="#fff" stroke-width="2"/></svg></div>
  <div class="arrow-btn" style="left:1024px"><svg width="12" height="12" viewBox="0 0 12 12"><path d="M4 1l5 5-5 5" fill="none" stroke="#fff" stroke-width="2"/></svg></div>
</section>

<section class="contact-band"></section>

<div class="contact-card">
  <p class="cc-kicker">CONTACT US TODAY</p>
  <h2 class="cc-title">We want to help you<br>transform your business.</h2>
  <p class="cc-text">Call us at +61 2 5550 1234 today. Fill out our contact form, or visit us,</p>
  <p class="cc-addr">Level 12, Harbour Point,<br>88 Quay Street,<br>Sydney NSW 2000 Australia</p>
  <div class="socials" style="left:330px;top:298px"><span></span><span></span><span></span><span></span></div>

  <span class="field-label" style="left:465px;top:40px">Your Name</span>
  <span class="field-label" style="left:672px;top:40px">Company</span>
  <div class="field" style="left:465px;top:56px;width:197px"></div>
  <div class="field" style="left:672px;top:56px;width:196px"></div>
  <span class="field-label" style="left:465px;top:102px">Email Address</span>
  <span class="field-label" style="left:672px;top:102px">Phone</span>
  <div class="field" style="left:465px;top:118px;width:197px"></div>
  <div class="field" style="left:672px;top:118px;width:196px"></div>
  <span class="field-label" style="left:465px;top:165px">Email Address</span>
  <div class="field" style="left:465px;top:181px;width:403px;height:84px"></div>
  <div class="btn-touch">GET IN TOUCH</div>
</div>

<footer class="site-footer">
  <p class="f-about">We help you make sure that an incident won’t affect in your business by providing you with the industry skills, expertise and knowledge to ensure that your business goes beyond mere compliance to business continuity and recovery standards, through to a workable plan.</p>
  <ul class="f-links" style="left:527px"><li>HOME</li><li>ABOUT</li><li>SERVICES</li><li>CLIENTS</li><li>RESOURCES</li><li>BLOG</li><li>CONTACT</li></ul>
  <div class="f-divider"></div>
  <ul class="f-links" style="left:637px"><li>TESTIMONIALS</li><li>MEET THE TEAM</li><li>PARTNERS</li><li>FAQ</li></ul>
  <div class="socials" style="left:992px;top:31px"><span></span><span></span><span></span><span></span></div>
  <p class="f-right" style="top:72px">+61 2 5550 1234</p>
  <p class="f-right" style="top:112px">Level 12, Harbour Point,<br>88 Quay Street,<br>Sydney NSW 2000 Australia</p>
  <div class="brand">
    <span class="brand-dot"></span>
    <div><span class="brand-name">taskharbor</span><span class="brand-tag">your trusted advisor</span></div>
  </div>
  <p class="copyright">© Copyright 2021. TASKHARBOR. All Rights Reserved.</p>
</footer>

</body>
</html>
```